Jewelry Business card for general purpose. Elegant and simple

We are a jewelry group with 6 stores in Mexico and 30 years in business.

We need a BC that at leats includes the name, mail, phone number and physical location (street, municipality, and county; example "Paseo Olmeda 2140", "Avenida Sotillo", "Monterrey").
Optional: we are trying to reposition the brand with the association of life-events or moments and family. Such as: birth, marriage, graduation, birthdays. Christmast, mothers day and fathers day.

We are looking for something elegant but simple

Jewelry name: "Lunetti". Email: "lunettibrillo@correo-ejemplo.mx". Phone num "4172-3095".

Target Market(s)

General business card: from suppliers to clients. One segment outstand: couples gettineg married

Industry/Entity Type

Jewelry Store

Contact Information for Business Card

Loking for something simple but elegant.

Font styles to use
Decorative
Script

Requirements
Must have
• Must have name, address, and mail.
Nice to have
• It could have jewelry pictures/design. Maybe quotes. Or general words as background . currently we have a very simple card with one ring would like to see something different.
Should not have
• Include real people.

```html
<!DOCTYPE html>
<html lang="es">
<head>
<meta charset="utf-8">
<title>Lunetti – Tarjeta de presentación</title>
<link rel="stylesheet" href="https://fonts.googleapis.com/css2?family=Open+Sans:wght@400;600&display=swap">
<style>
  :root {
    --backdrop: #efe9e1;
    --orange-deep: #f08a0c;
    --orange-mid: #f7b20f;
    --orange-dark: #e48a08;
    --gold-name: #c9891a;
    --ink: #1a1a1a;
    --ink-soft: #2b2b2b;
    --rule-red: #d9141c;
    --paper: #ffffff;
    --paper-shade: #eeeeee;
  }
  * { margin: 0; padding: 0; box-sizing: border-box; }
  html, body { width: 1200px; height: 900px; overflow: hidden; }
  body {
    background: var(--backdrop);
    font-family: "Open Sans", Arial, sans-serif;
    color: var(--ink);
    position: relative;
  }
  .card {
    position: absolute;
    width: 520px;
    height: 300px;
    overflow: hidden;
    box-shadow: 0 6px 18px rgba(0,0,0,0.18);
  }
  /* Back side */
  .card--back {
    left: 70px; top: 140px;
    background: linear-gradient(180deg, var(--orange-deep) 0%, var(--orange-mid) 45%, var(--orange-dark) 100%);
    display: flex; align-items: center; justify-content: center;
  }
  .brand-name {
    font-family: "Open Sans", Arial, sans-serif;
    font-weight: 600;
    font-size: 58px;
    letter-spacing: 1px;
    line-height: 1;
  }
  .card--back .brand-name { color: var(--ink); }

  /* Front side */
  .card--front {
    left: 610px; top: 460px;
    background: var(--paper);
  }
  .front-header {
    position: absolute; left: 0; top: 0; width: 100%; height: 140px;
    background: linear-gradient(180deg, var(--paper) 0%, var(--paper) 60%, var(--paper-shade) 100%);
    display: flex; align-items: center; justify-content: center;
  }
  .card--front .brand-name { color: var(--gold-name); font-size: 54px; }
  .accent-rule {
    position: absolute; left: 0; top: 140px; width: 100%; height: 3px;
    background: var(--rule-red);
  }
  .front-body {
    position: absolute; left: 0; top: 150px; width: 100%; height: 150px;
    background: linear-gradient(180deg, var(--orange-mid) 0%, var(--orange-mid) 40%, var(--orange-deep) 100%);
    color: var(--ink-soft);
  }
  .holder {
    position: absolute; left: 318px; top: 10px;
  }
  .holder-name { font-weight: 600; font-size: 17px; color: var(--ink); line-height: 1.2; }
  .holder-role { font-size: 12px; line-height: 1.3; }
  .contact-list {
    position: absolute; right: 232px; top: 44px;
    list-style: none; text-align: right;
  }
  .contact-list li {
    font-size: 14px; line-height: 24px;
    display: flex; align-items: center; justify-content: flex-end; gap: 8px;
  }
  .contact-list svg { width: 12px; height: 12px; fill: var(--ink); }
  .address {
    position: absolute; left: 0; width: 100%; top: 106px;
    text-align: center; font-size: 15px;
  }
</style>
</head>
<body>
  <section class="card card--back" aria-label="Reverso de la tarjeta">
    <span class="brand-name">Lunetti</span>
  </section>

  <section class="card card--front" aria-label="Frente de la tarjeta">
    <header class="front-header">
      <span class="brand-name">Lunetti</span>
    </header>
    <div class="accent-rule"></div>
    <div class="front-body">
      <div class="holder">
        <p class="holder-name">Mariana Ortega</p>
        <p class="holder-role">Managing Director</p>
      </div>
      <ul class="contact-list">
        <li>(044)-417-3095
          <svg viewBox="0 0 24 24" aria-hidden="true"><path d="M6.6 10.8a15.1 15.1 0 0 0 6.6 6.6l2.2-2.2a1 1 0 0 1 1-.25 11.4 11.4 0 0 0 3.6.57 1 1 0 0 1 1 1V20a1 1 0 0 1-1 1A17 17 0 0 1 3 4a1 1 0 0 1 1-1h3.5a1 1 0 0 1 1 1c0 1.25.2 2.45.57 3.57a1 1 0 0 1-.25 1z"/></svg>
        </li>
        <li>contacto@lunetti-joyas.mx
          <svg viewBox="0 0 24 24" aria-hidden="true"><path d="M2 5h20v14H2z M2 5l10 8 10-8" fill="currentColor"/><path d="M3 6l9 7 9-7" stroke="#f7b20f" stroke-width="2" fill="none"/></svg>
        </li>
      </ul>
      <p class="address">2140, Paseo Olmeda Avenida Sotillo, 64000</p>
    </div>
  </section>
</body>
</html>
```